Update Old OR create new Website

Current Website is looking a bit old, I did this one a few years back.

Would like a fresh new look, current website sitepress theme is " the Vanta theme" from plumcrate and I just purchased this theme - "bravlo" also from plumcrate, I quite like the look of - http://bravlo.quorvex-skins.com/tech-business/ and if we could get somthing simlar would be great.

current website is at http://www.hle.com.au, have been playing around with the slider that i like.

I have said 5 pages to be designed but really it is just a 5 page website where most pages will look the same.

Any questions please let me know

Target Market(s)

Business

Coding

Coded - Design and coding required

Number of Pages Required

5+ page

Font styles to use
Sans Serif

Colors
33a6d7
0292cd
ffffff
0255a3

Requirements
Must have
• Device compatibility - pc, tablet, phone
Nice to have
• video
Should not have
• vunerabilities. Must also use images that will expire or disappear, ie must be uploaded to site not links to elsewhere.

```html
<!DOCTYPE html>
<html lang="en">
<head>
<meta charset="utf-8">
<title>HLE Technologies – Whatever IT Takes</title>
<link href="https://fonts.googleapis.com/css2?family=Jost:wght@400;500&family=Lato:wght@400;700&display=swap" rel="stylesheet">
<style>
:root{
  --cyan:#00a9d9;
  --cyan-dark:#0292cd;
  --navy:#0255a3;
  --ink:#222222;
  --text:#444444;
  --muted:#777777;
  --line:#e2e2e2;
  --panel:#f2f2f2;
  --footer:#231f20;
  --footer-line:#3a3536;
  --white:#ffffff;
}
*{margin:0;padding:0;box-sizing:border-box}
html,body{width:1200px;height:2786px;overflow:hidden;background:var(--white)}
body{position:relative;font-family:'Lato',sans-serif;color:var(--text)}
.abs{position:absolute}
.heading{font-family:'Jost',sans-serif;font-weight:400}

/* top bar */
.topbar{left:0;top:0;width:1200px;height:37px;background:var(--cyan);color:var(--white);font-size:13px}
.topbar .item{position:absolute;top:10px;display:flex;align-items:center;gap:6px}

/* nav */
.nav{left:0;top:37px;width:1200px;height:82px;background:var(--white)}
.brand{position:absolute;left:121px;top:22px;display:flex;align-items:center;gap:10px}
.brand-mark{width:34px;height:34px;background:var(--cyan)}
.brand-name{font-family:'Jost',sans-serif;font-weight:500;font-size:22px;color:var(--ink)}
.nav-link{position:absolute;top:33px;font-size:13px;color:var(--ink)}
.nav-link.active{color:var(--cyan)}

/* hero */
.hero{left:0;top:119px;width:1200px;height:487px;background:linear-gradient(100deg,#1f2fc4 0%,#1d52c9 45%,#1a74a8 75%,#17924a 100%);color:var(--white);text-align:center}
.hero h1{position:absolute;left:0;width:1200px;top:170px;font-size:44px;line-height:52px}
.hero .rule{position:absolute;left:580px;top:234px;width:40px;height:2px;background:var(--white)}
.hero p{position:absolute;left:265px;width:670px;top:258px;font-size:12.5px;line-height:19px}

.btn{position:absolute;display:flex;height:32px;font-size:12px;font-weight:700;letter-spacing:.3px}
.btn .label{display:flex;align-items:center;padding:0 16px}
.btn .arrow{width:34px;display:flex;align-items:center;justify-content:center}
.btn-solid{background:var(--cyan);color:var(--white)}
.btn-solid .arrow{border-left:1px solid rgba(255,255,255,.6)}
.btn-outline{border:1px solid #bdbdbd;color:var(--ink);background:var(--white)}
.btn-outline .arrow{border-left:1px solid #bdbdbd}

/* services */
.service{top:660px;width:224px;height:241px;border:1px solid var(--line);text-align:center;background:var(--white)}
.service svg{position:absolute;left:86px;top:36px}
.service h3{position:absolute;left:0;width:100%;top:100px;font-family:'Lato',sans-serif;font-weight:400;font-size:16px;color:var(--ink)}
.service p{position:absolute;left:18px;right:18px;top:130px;font-size:12px;line-height:19px;color:var(--text)}
.service.featured{background:var(--cyan);border-color:var(--cyan);color:var(--white)}
.service.featured p{top:50px;color:var(--white)}
.service.featured .more{position:absolute;left:58px;top:144px;width:108px;height:30px;border:1px solid var(--white);color:var(--white);font-size:11px;font-weight:700;display:flex;align-items:center;justify-content:center}

/* support */
.support{left:0;top:955px;width:1200px;height:399px;background:var(--panel)}
.support .photo{position:absolute;left:176px;top:0;width:298px;height:399px;background:linear-gradient(180deg,#d8cfc8 0%,#b9a79b 45%,#8c8a8c 100%)}
.support h2{position:absolute;left:507px;top:78px;font-size:31px;line-height:40px;color:var(--ink)}
.support p{position:absolute;left:509px;top:175px;width:490px;font-size:13px;line-height:21px;color:var(--text)}

/* web */
.web{left:0;top:1354px;width:1200px;height:489px;background:var(--cyan)}
.web svg text{font-family:'Jost',sans-serif;fill:var(--white)}

/* apps */
.section-title{left:0;width:1200px;text-align:center;font-size:29px;color:var(--ink)}
.section-title .accent{color:var(--cyan)}
.title-rule{width:44px;height:2px;background:var(--ink)}
.app{top:1986px;width:224px;height:294px;background:var(--white);box-shadow:0 0 0 1px #eeeeee;text-align:center}
.app .shot{position:absolute;left:0;top:0;width:224px;height:132px}
.app .badge{position:absolute;left:88px;top:-26px;width:48px;height:48px;background:var(--ink);display:flex;align-items:center;justify-content:center}
.app.current .badge{background:var(--cyan)}
.app h3{position:absolute;left:0;width:100%;top:150px;font-family:'Lato',sans-serif;font-weight:400;font-size:15px;color:var(--ink)}
.app p{position:absolute;left:16px;right:16px;top:176px;font-size:12px;line-height:19px;color:var(--muted)}
.app .btn{left:46px;top:238px;height:32px;font-size:11px}
.app .bar{position:absolute;left:0;bottom:0;width:224px;height:3px;background:var(--ink)}
.app.current .bar{background:var(--cyan)}
.app.current .btn-outline{background:var(--cyan);border-color:var(--cyan);color:var(--white)}
.app.current .btn-outline .arrow{border-left-color:rgba(255,255,255,.6)}

/* clients */
.client{top:2332px;width:127px;height:59px;border:1px solid var(--line);display:flex;align-items:center;justify-content:center;font-family:'Lato',sans-serif;font-weight:700;font-size:17px;color:#3a3a3a}

/* footer */
.footer{left:0;top:2445px;width:1200px;height:341px;background:var(--footer);color:#cfcfcf;font-size:12px}
.footer h4{position:absolute;top:54px;font-family:'Lato',sans-serif;font-weight:400;font-size:15px;color:var(--white);letter-spacing:.3px}
.footer .col-rule{position:absolute;top:82px;height:1px;background:var(--footer-line)}
.footer .sep{position:absolute;top:60px;width:1px;height:190px;background:var(--footer-line)}
.quick-links{position:absolute;left:121px;top:100px;list-style:none}
.quick-links li{height:31px;font-size:12px;color:#d8d8d8}
.quick-links li::before{content:"›";margin-right:8px;color:#aaaaaa}
.contact-row{position:absolute;left:325px;display:flex;gap:10px;align-items:flex-start;line-height:16px}
.contact-row b{color:var(--white);font-weight:700}
.map{position:absolute;left:598px;top:104px;width:223px;height:128px;background:linear-gradient(135deg,#d9e6ee 0%,#c8dbe6 50%,#e3e7d6 100%);border:3px solid var(--white)}
.field{position:absolute;left:908px;width:172px;background:var(--white);color:#9a9a9a;font-size:10px;padding:6px 7px}
.submit{position:absolute;left:908px;top:227px;width:80px;height:26px;background:var(--cyan);color:var(--white);font-size:11px;font-weight:700;display:flex;align-items:center;justify-content:center}
.copyright{position:absolute;left:121px;top:312px;font-size:11px;color:#bdbdbd}
.social{position:absolute;top:306px;width:28px;height:28px;border-radius:50%;background:#3b5a9a}
</style>
</head>
<body>

<!-- top bar -->
<div class="abs topbar">
  <div class="item" style="left:845px">
    <svg width="13" height="13" viewBox="0 0 24 24"><path fill="#fff" d="M6.6 10.8a15.1 15.1 0 006.6 6.6l2.2-2.2c.3-.3.7-.4 1-.2 1.1.4 2.3.6 3.6.6.6 0 1 .4 1 1V20c0 .6-.4 1-1 1A17 17 0 013 4c0-.6.4-1 1-1h3.5c.6 0 1 .4 1 1 0 1.3.2 2.5.6 3.6.1.3 0 .7-.2 1z"/></svg>
    1300 555 018
  </div>
  <div class="item" style="left:966px">
    <svg width="14" height="11" viewBox="0 0 24 18"><rect x="1" y="1" width="22" height="16" fill="none" stroke="#fff" stroke-width="2"/><path d="M1 1l11 9 11-9" fill="none" stroke="#fff" stroke-width="2"/></svg>
    info@hle.com.au
  </div>
</div>

<!-- navigation -->
<header class="abs nav">
  <div class="brand"><span class="brand-mark"></span><span class="brand-name">HLE Technologies</span></div>
  <span class="nav-link active" style="left:480px">Home</span>
  <span class="nav-link" style="left:605px">Our Services <svg width="8" height="6" viewBox="0 0 8 6"><path d="M1 1l3 3 3-3" fill="none" stroke="#222" stroke-width="1.3"/></svg></span>
  <span class="nav-link" style="left:772px">Web</span>
  <span class="nav-link" style="left:890px">APP's</span>
  <span class="nav-link" style="left:1012px">Contact Us</span>
</header>

<!-- hero -->
<section class="abs hero" role="img" aria-label="Blurred screen of program code over a blue to green gradient">
  <h1 class="heading">WhateverIT TAKES</h1>
  <div class="rule"></div>
  <p>With over  a decade of experience, HLE Technologies understands the challenges faced by SMEs. So when we design and build networks, support solutions, hardware and software we improve the performance of your organisation</p>
  <div class="btn btn-solid" style="left:530px;top:312px"><span class="label">CONTACT US</span><span class="arrow"><svg width="14" height="10" viewBox="0 0 14 10"><path d="M0 5h12M8 1l4 4-4 4" fill="none" stroke="#fff" stroke-width="1.4"/></svg></span></div>
</section>

<!-- services -->
<div class="abs service" style="left:121px">
  <svg width="52" height="48" viewBox="0 0 52 48"><g fill="var(--cyan)"><rect x="2" y="2" width="48" height="12" rx="1"/><rect x="2" y="18" width="48" height="12" rx="1"/><rect x="2" y="34" width="48" height="12" rx="1"/></g><g fill="#fff"><circle cx="9" cy="8" r="2"/><circle cx="9" cy="24" r="2"/><circle cx="9" cy="40" r="2"/><rect x="30" y="7" width="15" height="2"/><rect x="30" y="23" width="15" height="2"/><rect x="30" y="39" width="15" height="2"/></g></svg>
  <h3>Servers</h3>
  <p>HLE Technologies provides the design, support and maintenance for quality I.T Systems for clients to thrive, change and grow.</p>
</div>
<div class="abs service featured" style="left:364px">
  <p>HLE team members take great pride in their depth of understanding of their client's industries and business models.  This knowledge</p>
  <div class="more">READ MORE</div>
</div>
<div class="abs service" style="left:611px">
  <svg width="56" height="48" viewBox="0 0 56 48"><path d="M14 34a10 10 0 010-20 14 14 0 0127-3 10 10 0 011 20" fill="none" stroke="var(--cyan)" stroke-width="3"/><circle cx="24" cy="34" r="6" fill="none" stroke="var(--cyan)" stroke-width="3"/><circle cx="38" cy="38" r="5" fill="none" stroke="var(--cyan)" stroke-width="3"/><path d="M24 25v3M24 40v3M15 34h3M30 34h3M38 30v2M38 44v2M31 38h2M43 38h2" stroke="var(--cyan)" stroke-width="3"/></svg>
  <h3>Managed IT</h3>
  <p>HLE team members take great pride in their depth of understanding of their client's industries and business models.  This knowledge</p>
</div>
<div class="abs service" style="left:857px">
  <svg width="52" height="52" viewBox="0 0 52 52"><g fill="none" stroke="var(--cyan)" stroke-width="2.5"><circle cx="24" cy="24" r="21"/><ellipse cx="24" cy="24" rx="9" ry="21"/><path d="M3 24h42M6 13h36M6 35h36M24 3v42"/></g><path d="M34 32l14 6-6 2-2 6z" fill="var(--white)" stroke="var(--cyan)" stroke-width="2.5" stroke-linejoin="round"/></svg>
  <h3>Internet</h3>
  <p>Having access to the leading providers of Internet in Australia we can determine not only who will give you the fastest connection.</p>
</div>

<!-- support -->
<section class="abs support">
  <div class="photo" role="img" aria-label="Photo of a smiling support agent wearing a headset, arms crossed"></div>
  <h2 class="heading">Need Any Help? Our 5-Star Support<br>Will Help You.</h2>
  <p>Lorem ipsum dolor sit amet, consectetuer adipiscing elit, sed diam nonummy nibh euismod tincidunt ut laoreet dolore magna aliquam erat volutpat. Ut wisi enim ad minim veniam</p>
  <div class="btn btn-outline" style="left:509px;top:255px"><span class="label">CONTACT US</span><span class="arrow"><svg width="14" height="10" viewBox="0 0 14 10"><path d="M0 5h12M8 1l4 4-4 4" fill="none" stroke="#444" stroke-width="1.4"/></svg></span></div>
</section>

<!-- web services -->
<section class="abs web">
  <svg width="1200" height="489" viewBox="0 0 1200 489">
    <text x="600" y="64" text-anchor="middle" font-size="29">Web</text>
    <rect x="580" y="80" width="40" height="2" fill="#fff"/>
    <circle cx="611" cy="430" r="245" fill="none" stroke="#fff" stroke-width="6"/>
    <g fill="var(--cyan)" stroke="#fff" stroke-width="4">
      <rect x="341" y="396" width="50" height="50"/>
      <rect x="360" y="309" width="50" height="50"/>
      <rect x="407" y="238" width="50" height="50"/>
      <rect x="486" y="181" width="50" height="50"/>
      <rect x="586" y="160" width="50" height="50"/>
      <rect x="686" y="181" width="50" height="50"/>
      <rect x="765" y="238" width="50" height="50"/>
      <rect x="812" y="309" width="50" height="50"/>
      <rect x="831" y="396" width="50" height="50"/>
    </g>
    <g fill="none" stroke="#fff" stroke-width="2.2">
      <rect x="354" y="410" width="24" height="17"/><path d="M362 432h8M366 427v5"/>
      <circle cx="385" cy="334" r="3"/><circle cx="376" cy="325" r="2.5"/><circle cx="395" cy="326" r="2.5"/><circle cx="377" cy="343" r="2.5"/><path d="M383 332l-5-5M387 332l6-5M383 337l-5 4"/>
      <rect x="420" y="253" width="24" height="18"/><path d="M425 259h14M425 265h9"/>
      <path d="M500 201h5l12-7v22l-12-7h-5z"/><path d="M521 200l4-3M522 206h5"/>
      <circle cx="609" cy="183" r="7"/><path d="M614 188l7 7"/><rect x="598" y="172" width="26" height="26"/>
      <circle cx="708" cy="205" r="10"/><circle cx="708" cy="205" r="4"/><path d="M711 202l8-8"/>
      <circle cx="790" cy="263" r="11"/><path d="M784 263a6 6 0 0110-4M796 263a6 6 0 01-10 4"/>
      <path d="M827 344l14-14 4 4-14 14-6 2z"/>
      <path d="M844 413h22v13h-12l-6 5v-5h-4z"/>
    </g>
    <rect x="511" y="318" width="201" height="93" rx="3" fill="#fff"/>
    <rect x="530" y="352" width="22" height="22" fill="var(--cyan)"/>
    <text x="562" y="371" font-size="19" style="fill:var(--ink)" font-weight="500">HLE Technologies</text>
    <g font-size="20">
      <text x="321" y="430" text-anchor="end">Website Design</text>
      <text x="344" y="340" text-anchor="end">Digital Strategy</text>
      <text x="392" y="246" text-anchor="end">Content</text>
      <text x="392" y="267" text-anchor="end">Management Systems</text>
      <text x="470" y="179" text-anchor="end">Web Marketing</text>
      <text x="611" y="131" text-anchor="middle">SEO</text>
      <text x="758" y="179">Pay Per Click</text>
      <text x="838" y="248">Remarketing</text>
      <text x="886" y="340">Copywriting</text>
      <text x="899" y="430">Social Media</text>
      <text x="899" y="451">Management</text>
    </g>
  </svg>
</section>

<!-- apps -->
<h2 class="abs section-title heading" style="top:1886px">APP’<span class="accent">s</span></h2>
<div class="abs title-rule" style="left:578px;top:1934px"></div>

<article class="abs app" style="left:121px">
  <div class="shot" role="img" aria-label="Photo of a team arranging cards around a wooden table" style="background:linear-gradient(135deg,#6b5a4c,#a39686)"></div>
  <div class="badge"><svg width="24" height="24" viewBox="0 0 24 24"><circle cx="10" cy="10" r="7" fill="none" stroke="#fff" stroke-width="2.4"/><path d="M15 15l7 7" stroke="#fff" stroke-width="2.4"/></svg></div>
  <h3>Discovery &amp; Strategy</h3>
  <p>Lorem ipsum dolor sit amet, consectetuer adipiscing elit, sed diam nonummy nibh euismod</p>
  <div class="btn btn-outline"><span class="label">READ MORE</span><span class="arrow"><svg width="14" height="10" viewBox="0 0 14 10"><path d="M0 5h12M8 1l4 4-4 4" fill="none" stroke="currentColor" stroke-width="1.4"/></svg></span></div>
  <div class="bar"></div>
</article>
<article class="abs app current" style="left:364px">
  <div class="shot" role="img" aria-label="Photo of hands sketching interface layouts on paper at a desk" style="background:linear-gradient(135deg,#e9e4dc,#b9a68e)"></div>
  <div class="badge"><svg width="24" height="22" viewBox="0 0 24 22"><rect x="2" y="2" width="20" height="14" fill="none" stroke="#fff" stroke-width="2"/><path d="M8 20h8M12 16v4" stroke="#fff" stroke-width="2"/></svg></div>
  <h3>User Experience Design</h3>
  <p>Lorem ipsum dolor sit amet, consectetuer adipiscing elit, sed diam nonummy nibh euismod</p>
  <div class="btn btn-outline"><span class="label">READ MORE</span><span class="arrow"><svg width="14" height="10" viewBox="0 0 14 10"><path d="M0 5h12M8 1l4 4-4 4" fill="none" stroke="currentColor" stroke-width="1.4"/></svg></span></div>
  <div class="bar"></div>
</article>
<article class="abs app" style="left:611px">
  <div class="shot" role="img" aria-label="Photo of a smartphone in front of a chalkboard with app sketches" style="background:linear-gradient(135deg,#4a403a,#8b7c70)"></div>
  <div class="badge"><svg width="18" height="26" viewBox="0 0 18 26"><rect x="2" y="2" width="14" height="22" rx="2" fill="none" stroke="#fff" stroke-width="2"/><circle cx="9" cy="19" r="1.5" fill="#fff"/></svg></div>
  <h3>Mobile App Development</h3>
  <p>Lorem ipsum dolor sit amet, consectetuer adipiscing elit, sed diam nonummy nibh euismod</p>
  <div class="btn btn-outline"><span class="label">READ MORE</span><span class="arrow"><svg width="14" height="10" viewBox="0 0 14 10"><path d="M0 5h12M8 1l4 4-4 4" fill="none" stroke="currentColor" stroke-width="1.4"/></svg></span></div>
  <div class="bar"></div>
</article>
<article class="abs app" style="left:857px">
  <div class="shot" role="img" aria-label="Photo of colleagues reviewing work together at a computer" style="background:linear-gradient(135deg,#3c4148,#9aa3aa)"></div>
  <div class="badge"><svg width="24" height="22" viewBox="0 0 24 22"><rect x="2" y="2" width="20" height="14" fill="none" stroke="#fff" stroke-width="2"/><path d="M7 9l3 3 6-6" fill="none" stroke="#fff" stroke-width="2"/><path d="M8 20h8" stroke="#fff" stroke-width="2"/></svg></div>
  <h3>Testing &amp; Deployment</h3>
  <p>Lorem ipsum dolor sit amet, consectetuer adipiscing elit, sed diam nonummy nibh euismod</p>
  <div class="btn btn-outline"><span class="label">READ MORE</span><span class="arrow"><svg width="14" height="10" viewBox="0 0 14 10"><path d="M0 5h12M8 1l4 4-4 4" fill="none" stroke="currentColor" stroke-width="1.4"/></svg></span></div>
  <div class="bar"></div>
</article>

<!-- clients -->
<div class="abs client" style="left:121px">Ledgerly</div>
<div class="abs client" style="left:260px">Leafhop</div>
<div class="abs client" style="left:399px">nodewise</div>
<div class="abs client" style="left:537px">Tramora</div>
<div class="abs client" style="left:676px">VAULTLINE</div>
<div class="abs client" style="left:815px">Beacona</div>
<div class="abs client" style="left:953px">CORVANE</div>

<!-- footer -->
<footer class="abs footer">
  <h4 style="left:121px">QUICK LINKS</h4>
  <div class="col-rule" style="left:121px;width:140px"></div>
  <ul class="quick-links">
    <li>Home</li><li>Our Services</li><li>Web</li><li>App's</li><li>Contact Us</li>
  </ul>
  <div class="sep" style="left:282px"></div>

  <h4 style="left:325px">CONTACT DETAILS</h4>
  <div class="col-rule" style="left:325px;width:190px"></div>
  <div class="contact-row" style="top:100px">
    <svg width="11" height="15" viewBox="0 0 12 16"><path d="M6 0a6 6 0 00-6 6c0 4.5 6 10 6 10s6-5.5 6-10a6 6 0 00-6-6zm0 8.5A2.5 2.5 0 116 3.5a2.5 2.5 0 010 5z" fill="#fff"/></svg>
    <div><b>HLE Technologies<br>Information Technology</b><br><span style="display:block;margin-top:8px">14 Ridgeway Ave,<br>Eastfield</span></div>
  </div>
  <div class="contact-row" style="top:184px">
    <svg width="12" height="12" viewBox="0 0 24 24"><path fill="#fff" d="M6.6 10.8a15.1 15.1 0 006.6 6.6l2.2-2.2c.3-.3.7-.4 1-.2 1.1.4 2.3.6 3.6.6.6 0 1 .4 1 1V20c0 .6-.4 1-1 1A17 17 0 013 4c0-.6.4-1 1-1h3.5c.6 0 1 .4 1 1 0 1.3.2 2.5.6 3.6.1.3 0 .7-.2 1z"/></svg>
    <b>1300 555 018</b>
  </div>
  <div class="contact-row" style="top:219px">
    <svg width="12" height="10" viewBox="0 0 24 18"><rect x="1" y="1" width="22" height="16" fill="none" stroke="#fff" stroke-width="2"/><path d="M1 1l11 9 11-9" fill="none" stroke="#fff" stroke-width="2"/></svg>
    info@hle.com.au
  </div>
  <div class="sep" style="left:552px"></div>

  <h4 style="left:598px">LOCATION MAP</h4>
  <div class="col-rule" style="left:598px;width:223px"></div>
  <div class="map" role="img" aria-label="Street map of the office location with a red pin"></div>
  <div class="sep" style="left:864px"></div>

  <h4 style="left:908px">CONTACT NOW</h4>
  <div class="col-rule" style="left:908px;width:172px"></div>
  <div class="field" style="top:102px;height:25px">Your Name</div>
  <div class="field" style="top:136px;height:24px">Your Email</div>
  <div class="field" style="top:167px;height:47px">Message</div>
  <div class="submit">SUBMIT</div>

  <div class="copyright">Copyright © 2017 HLE Technologies Information Technology. All Rights Reserved.</div>
  <div class="social" style="left:939px" aria-label="Social link"></div>
  <div class="social" style="left:976px;background:#1e78b4" aria-label="Social link"></div>
  <div class="social" style="left:1013px;background:#1da1f2" aria-label="Social link"></div>
  <div class="social" style="left:1052px;background:#dd4b39" aria-label="Social link"></div>
</footer>

</body>
</html>
```